Book cover for book of Poems "Lanternfall"

I have written a book of poems. The book is titled "Lanternfall" and has 160 pages. The poems were written mostly during my youth but there are newer poems also written over the past 10 years (I'm 42 now). They are mostly about love, loss, social conformity, and nature. I'm influenced a lot by the English Romantic Poets, gothic motives, and 80s music by bands such as The Vells, Corabel & the Tarrows, and Pennock. I need an original book cover design for my book. Attached are samples of designs I like and few of my poems. The cover will be a hardcover and I need design for Front Cover, Back Cover, and Spine. Dimension is 6"x9". Front Cover should have name of book "Lanternfall" and name of author "Ravi Menhar". Thanks.
Updates

Further details which I should have included in my original brief -The book cover will be a hard cover. Design is required for front cover, back cover, and spine. Dimension is 6x9.Front should have book title "Lanternfall" and author's name "Ravi Menhar". Added Monday, December 19, 2016

Target Market(s)

Mostly friends and family

Requirements
Must have
• I don't mind a design where lanternfall is spelled out in big capital letters and text from one of my poems is inside, like the sample I've attached.

```html
<!DOCTYPE html>
<html lang="en">
<head>
<meta charset="utf-8">
<title>Lanternfall — Ravi Menhar</title>
<link href="https://fonts.googleapis.com/css2?family=Anton&family=Oswald:wght@300;400&display=swap" rel="stylesheet">
<style>
  :root {
    --stage: #c9d0d1;
    --slate: #3d4454;
    --slate-deep: #363c4a;
    --dusk: #5b5f66;
    --amber: #e9a040;
    --glow: #f7b23a;
    --title-gold: #efa81b;
    --rule-gold: #c9962a;
    --ink-light: #f4f4f2;
    --earth: #1a1612;
  }
  * { box-sizing: border-box; margin: 0; padding: 0; }
  html, body {
    width: 1200px;
    height: 958px;
    overflow: hidden;
    background: var(--stage);
  }
  .stage {
    width: 1200px;
    height: 958px;
    display: flex;
    align-items: center;
    justify-content: center;
  }
  .front-cover {
    position: relative;
    width: 570px;
    height: 880px;
    background: linear-gradient(180deg, var(--slate-deep) 0%, var(--slate) 45%);
    overflow: hidden;
  }
  .cover-photo {
    position: absolute;
    left: 0;
    right: 0;
    top: 360px;
    bottom: 0;
    background:
      radial-gradient(ellipse 55% 35% at 55% 98%, var(--glow) 0%, rgba(247,178,58,0) 70%),
      linear-gradient(180deg, var(--slate) 0%, var(--dusk) 35%, #a98350 65%, var(--amber) 85%, var(--earth) 100%);
  }
  .author-line {
    position: absolute;
    top: 72px;
    left: 18px;
    right: 18px;
    display: flex;
    align-items: center;
    gap: 12px;
  }
  .author-line .rule {
    flex: 1;
    height: 1px;
    background: var(--rule-gold);
  }
  .author-name {
    font-family: "Oswald", sans-serif;
    font-weight: 400;
    font-size: 38px;
    letter-spacing: 0.28em;
    margin-right: -0.28em;
    color: var(--ink-light);
    line-height: 1;
    white-space: nowrap;
  }
  .book-title {
    position: absolute;
    top: 150px;
    left: 0;
    right: 0;
    text-align: center;
    font-family: "Anton", sans-serif;
    font-size: 86px;
    line-height: 1;
    letter-spacing: 0.01em;
    color: var(--title-gold);
  }
</style>
</head>
<body>
  <main class="stage">
    <section class="front-cover">
      <div class="cover-photo" role="img" aria-label="Photograph: silhouette of a child with outstretched arms riding on a parent's shoulders against a sunset sky over tall grass"></div>
      <div class="author-line">
        <span class="rule"></span>
        <span class="author-name">RAVI MENHAR</span>
        <span class="rule"></span>
      </div>
      <h1 class="book-title">LANTERNFALL</h1>
    </section>
  </main>
</body>
</html>
```